PINE HOLLOW BUILDERS leave behind sales FLYER 8.5"x11"

We need a high quality advertising flyer 8.5"x11" for our construction company offering kitchen and bathroom remodels. Can be front and back or just the front of the flyer depending on the design. phone number to come
www.brightmortarworks.example

we are also a home inspection company. We will leave this at the home when we are done with our home inspections for our new home owners

Target Market(s)

Home owners

Industry/Entity Type

Residential Construction

Contact Information for Business Card

We want it to match the flyer please

Requirements
Must have
• My logo, my website , my phone number (to come later),
• FL State Lic. #CRC8047163 & Insured
• We Specialize in Bathroom and Kitchen remodeling ,new Construction & Interior or Exterior home Renovations, garages and more! Serving Central Florida for over 15 years.
• Family owned and operated,
• we perform all levels of building and remodeling.
• i wouldn't mind seeing what you come up with for text on the flyer.
Nice to have
• maybe a nice kitchen and bathroom pictures

```html
<!DOCTYPE html>
<html lang="en">
<head>
<meta charset="utf-8">
<title>Pine Hollow Builders – Home Renovation Flyer</title>
<link rel="stylesheet" href="https://fonts.googleapis.com/css2?family=Bebas+Neue&family=Open+Sans:wght@400;600&display=swap">
<style>
  :root {
    --orange: #f39422;
    --ink: #111111;
    --paper: #ffffff;
    --band-grey: #e4e4e4;
    --logo-grey: #4a4a4a;
    --blueprint: #eef2f6;
  }
  * { margin: 0; padding: 0; box-sizing: border-box; }
  html, body { width: 991px; height: 1200px; overflow: hidden; background: var(--paper); }
  .flyer {
    position: relative;
    width: 991px; height: 1200px;
    background: linear-gradient(160deg, var(--paper) 0%, var(--blueprint) 55%, var(--paper) 100%);
    font-family: "Open Sans", sans-serif;
    color: var(--ink);
    overflow: hidden;
  }
  .blueprint-backdrop {
    position: absolute; left: 380px; top: 180px; width: 611px; height: 560px;
    background: radial-gradient(ellipse at 60% 40%, #e6ecf2 0%, rgba(255,255,255,0) 70%);
  }
  .headline {
    position: absolute; left: 60px; top: 54px; z-index: 2;
    font-family: "Bebas Neue", sans-serif;
    font-size: 110px; line-height: 92px; letter-spacing: 1px;
    font-weight: 400;
  }
  .intro {
    position: absolute; left: 58px; top: 356px; width: 495px; z-index: 2;
    font-size: 18px; line-height: 27px; font-weight: 600;
  }
  .worker-photo {
    position: absolute; left: 560px; top: 173px; width: 431px; height: 804px;
    background: linear-gradient(180deg, #f6d24a 0%, #c98a5e 22%, #e8662a 45%, #e35a22 70%, #6f86a8 100%);
    border-radius: 200px 160px 0 0 / 320px 160px 0 0;
  }
  .services-bar {
    position: absolute; left: 0; top: 485px; width: 544px; height: 65px; z-index: 2;
    background: var(--orange);
    font-family: "Bebas Neue", sans-serif; font-weight: 400;
    font-size: 46px; line-height: 65px; padding-left: 60px;
  }
  .service-list {
    position: absolute; left: 60px; top: 580px; list-style: none;
    font-size: 24px; line-height: 32px;
  }
  .service-list li { display: flex; align-items: center; gap: 12px; }
  .service-list svg { width: 17px; height: 17px; flex: none; }
  .guarantee {
    position: absolute; left: 60px; top: 845px;
    font-family: "Bebas Neue", sans-serif; font-size: 38px; line-height: 40px;
  }
  .phone {
    position: absolute; left: 60px; top: 890px;
    display: flex; align-items: center; gap: 12px;
    font-family: "Bebas Neue", sans-serif; font-size: 72px; line-height: 72px;
  }
  .phone svg { width: 54px; height: 54px; }
  .gallery-band {
    position: absolute; left: 0; top: 977px; width: 991px; height: 176px;
    background: var(--band-grey);
  }
  .gallery-photo {
    position: absolute; top: 20px; width: 208px; height: 136px;
    border: 7px solid var(--paper);
    box-shadow: 0 2px 6px rgba(0,0,0,0.35);
    transform: rotate(-2deg);
  }
  .gallery-photo.living { left: 22px; background: linear-gradient(135deg, #d9d6cf, #a59c90); }
  .gallery-photo.kitchen { left: 239px; background: linear-gradient(135deg, #4a3a30, #bfb8ae); }
  .gallery-photo.bath { left: 456px; background: linear-gradient(135deg, #6d6256, #2e2c2a); }
  .brand {
    position: absolute; left: 705px; top: 40px; width: 250px;
    display: flex; flex-direction: column; align-items: center; gap: 12px;
  }
  .brand-mark { width: 62px; height: 62px; background: var(--orange); }
  .brand-name {
    font-family: "Bebas Neue", sans-serif; font-size: 32px; letter-spacing: 2px;
    color: var(--logo-grey); white-space: nowrap;
  }
  .footer-bar {
    position: absolute; left: 0; top: 1153px; width: 991px; height: 47px;
    background: var(--orange);
    display: flex; align-items: center; justify-content: space-between;
    padding: 0 40px 0 36px;
  }
  .footer-left { display: flex; align-items: center; }
  .social { display: flex; gap: 4px; align-items: center; }
  .social span { width: 22px; height: 22px; background: var(--ink); display: block; }
  .website { font-family: "Bebas Neue", sans-serif; font-size: 23px; margin-left: 14px; }
  .license { font-size: 13px; font-style: italic; }
</style>
</head>
<body>
  <main class="flyer">
    <div class="blueprint-backdrop" role="img" aria-label="Faint architectural floor plan in the background"></div>

    <div class="worker-photo" role="img" aria-label="Smiling construction worker in a yellow hard hat and orange safety vest with arms crossed"></div>

    <h1 class="headline">Home Renovation and<br>Construction<br>Service</h1>

    <p class="intro">We Specialize in New Construction &amp; Interior or Exterior home Renovations, Including Bathroom and kitchen remodeling, garages and more! Family owned and operated.</p>

    <h2 class="services-bar">Our Services</h2>

    <ul class="service-list">
      <li><svg viewBox="0 0 17 17"><rect x="1" y="3" width="12" height="12" rx="2" fill="none" stroke="#111" stroke-width="2"/><path d="M4 8.5l3 3 8-9" fill="none" stroke="#111" stroke-width="2.2"/></svg>New Construction</li>
      <li><svg viewBox="0 0 17 17"><rect x="1" y="3" width="12" height="12" rx="2" fill="none" stroke="#111" stroke-width="2"/><path d="M4 8.5l3 3 8-9" fill="none" stroke="#111" stroke-width="2.2"/></svg>Barns</li>
      <li><svg viewBox="0 0 17 17"><rect x="1" y="3" width="12" height="12" rx="2" fill="none" stroke="#111" stroke-width="2"/><path d="M4 8.5l3 3 8-9" fill="none" stroke="#111" stroke-width="2.2"/></svg>Remodels</li>
      <li><svg viewBox="0 0 17 17"><rect x="1" y="3" width="12" height="12" rx="2" fill="none" stroke="#111" stroke-width="2"/><path d="M4 8.5l3 3 8-9" fill="none" stroke="#111" stroke-width="2.2"/></svg>Renovations</li>
      <li><svg viewBox="0 0 17 17"><rect x="1" y="3" width="12" height="12" rx="2" fill="none" stroke="#111" stroke-width="2"/><path d="M4 8.5l3 3 8-9" fill="none" stroke="#111" stroke-width="2.2"/></svg>Repairs</li>
      <li><svg viewBox="0 0 17 17"><rect x="1" y="3" width="12" height="12" rx="2" fill="none" stroke="#111" stroke-width="2"/><path d="M4 8.5l3 3 8-9" fill="none" stroke="#111" stroke-width="2.2"/></svg>Kitchens</li>
      <li><svg viewBox="0 0 17 17"><rect x="1" y="3" width="12" height="12" rx="2" fill="none" stroke="#111" stroke-width="2"/><path d="M4 8.5l3 3 8-9" fill="none" stroke="#111" stroke-width="2.2"/></svg>Bathrooms</li>
      <li><svg viewBox="0 0 17 17"><rect x="1" y="3" width="12" height="12" rx="2" fill="none" stroke="#111" stroke-width="2"/><path d="M4 8.5l3 3 8-9" fill="none" stroke="#111" stroke-width="2.2"/></svg>Bank Remodels</li>
    </ul>

    <p class="guarantee">Quality Construction Guaranteed</p>

    <p class="phone">
      <svg viewBox="0 0 56 56"><circle cx="28" cy="28" r="25" fill="none" stroke="#111" stroke-width="4"/><path d="M19 15c-3 2-4 6-1 12s9 12 15 14c4 1 6 0 8-3l-5-5-4 3c-4-2-7-5-9-9l3-4z" fill="#111"/></svg>
      (555) 014-2286
    </p>

    <section class="gallery-band">
      <div class="gallery-photo living" role="img" aria-label="Renovated living room with white tile floor and stone fireplace"></div>
      <div class="gallery-photo kitchen" role="img" aria-label="Remodeled kitchen with dark cabinets and stainless appliances"></div>
      <div class="gallery-photo bath" role="img" aria-label="Remodeled bathroom with double vanity and round mirrors"></div>
      <div class="brand">
        <span class="brand-mark"></span>
        <span class="brand-name">PINE HOLLOW BUILDERS</span>
      </div>
    </section>

    <footer class="footer-bar">
      <div class="footer-left">
        <div class="social"><span></span><span></span></div>
        <span class="website">WWW.BRIGHTMORTARWORKS.EXAMPLE</span>
      </div>
      <span class="license">FL State Lic. # CRC8047163 &amp; Insured</span>
    </footer>
  </main>
</body>
</html>
```